Newsletter Design Project

I need a new design for a monthly newsletter that I do for Academy of Lifelong Pursuits Brisbane. I have been doing the same thing since 2009. We are based in Brisbane and we run classes for semi retired and retired people. I write about social activities, class activities, vacancies etc. I take photos and include them we hhave a logo that I always use. and would just like the newsletter to look different and fresh. The logo is Blue

```html
<!DOCTYPE html>
<html lang="en">
<head>
<meta charset="utf-8">
<title>E Newsletter – Month 2013</title>
<link rel="stylesheet" href="https://fonts.googleapis.com/css2?family=Tinos:wght@400;700&display=swap">
<style>
  :root {
    --sky-deep: #0b7fbf;
    --sky-mid: #2a9ad3;
    --sky-light: #9fd3ee;
    --paper: #ffffff;
    --ink: #111111;
    --rule: #1d1d1d;
    --logo-frame: #22395a;
    --placeholder-light: #f2f3f5;
    --placeholder-shade: #dfe2e6;
  }
  * { box-sizing: border-box; margin: 0; padding: 0; }
  html, body { width: 848px; height: 1200px; overflow: hidden; }
  body {
    position: relative;
    font-family: "Tinos", "Times New Roman", serif;
    color: var(--ink);
    background:
      linear-gradient(160deg, rgba(255,255,255,0.45) 0%, rgba(255,255,255,0) 35%),
      linear-gradient(180deg, var(--sky-light) 0%, var(--sky-mid) 30%, var(--sky-deep) 100%);
  }
  .masthead {
    position: absolute; left: 52px; top: 50px; width: 746px; height: 223px;
    background: var(--paper);
  }
  .masthead__photo {
    position: absolute; top: 14px; width: 148px; height: 206px;
    background: linear-gradient(180deg, var(--placeholder-light) 0%, var(--placeholder-shade) 100%);
  }
  .masthead__photo--left { left: 0; }
  .masthead__photo--right { right: 0; }
  .masthead__logo {
    position: absolute; left: 311px; top: 12px; width: 130px; height: 70px;
    border: 3px solid var(--logo-frame);
  }
  .masthead__title, .masthead__issue {
    position: absolute; left: 0; width: 100%; text-align: center;
    font-weight: 700; font-size: 22px; line-height: 26px;
  }
  .masthead__title { top: 91px; }
  .masthead__issue { top: 130px; }
  .headline-band {
    position: absolute; background: var(--paper);
    border-top: 2px solid var(--rule); border-bottom: 2px solid var(--rule);
    display: flex; align-items: center; justify-content: center;
  }
  .headline-band h2 { font-size: 30.5px; font-weight: 700; letter-spacing: 0.3px; }
  .headline-band--lead { left: 52px; top: 294px; width: 746px; height: 107px; }
  .headline-band--feature { left: 299px; top: 763px; width: 499px; height: 92px; }
  .article {
    position: absolute; background: var(--paper);
    font-size: 16px; line-height: 22.6px; text-align: justify;
  }
  .article p + p { margin-top: 7px; }
  .article--lead { left: 52px; top: 420px; width: 746px; height: 320px; padding: 4px 11px 0 11px; }
  .article--feature { left: 299px; top: 871px; width: 499px; height: 277px; padding: 4px 11px 0 12px; }
  .feature-photo {
    position: absolute; left: 52px; top: 762px; width: 228px; height: 386px;
    background: linear-gradient(180deg, var(--placeholder-light) 0%, var(--placeholder-shade) 100%);
    border: 1px solid #cfcfcf;
  }
</style>
</head>
<body>
  <header class="masthead">
    <div class="masthead__photo masthead__photo--left" role="img" aria-label="Photo of a stack of colourful books"></div>
    <div class="masthead__logo" role="img" aria-label="Logo space"></div>
    <p class="masthead__title">E Newsletter</p>
    <p class="masthead__issue">Month 2013</p>
    <div class="masthead__photo masthead__photo--right" role="img" aria-label="Photo of a stack of colourful books"></div>
  </header>

  <div class="headline-band headline-band--lead"><h2>LOREM IPSUM</h2></div>

  <article class="article article--lead">
    <p>Lorem ipsum dolor sit amet, consectetur adipiscing elit. Aliquam semper metus id blandit posuere. Duis sem urna, vulputate et aliquam feugiat, sagittis nec tortor. Nunc erat diam, pharetra nec est ac, faucibus adipiscing ligula. Quisque vulputate nulla nisi. Aenean elit elit, luctus sit amet leo vitae, aliquam venenatis est. Mauris sollicitudin non eros vel aliquam. Phasellus rutrum mi nec risus imperdiet viverra. Morbi ut mauris quis metus ornare aliquam. Aenean metus risus, tincidunt sed tellus vel, ullamcorper gravida mi. Suspendisse ultrices erat id ipsum laoreet, eget luctus erat eleifend. Sed ac ipsum ligula. Sed volutpat sapien sit amet tellus condimentum, sed porttitor leo sollicitudin. Suspendisse porta lorem massa, non faucibus erat ultricies sit amet. Nullam ac libero id ipsum elementum aliquam. Praesent diam ligula, pretium id iaculis nec, aliquet in sapien.</p>
    <p>Maecenas sed sodales sem, sit amet viverra ipsum. Duis ut lacus egestas, egestas nunc at, feugiat metus. Fusce in ultrices enim. Nam gravida tortor vulputate libero vestibulum auctor. Proin elementum ornare lectus, vel feugiat nisl molestie sit amet. Donec venenatis eros non purus adipiscing, a condimentum ante adipiscing. Mauris aliquet eget nulla in varius.</p>
  </article>

  <div class="feature-photo" role="img" aria-label="Illustration of a thoughtful figure sitting beside a stack of colourful books"></div>

  <div class="headline-band headline-band--feature"><h2>LOREM IPSUM</h2></div>

  <article class="article article--feature">
    <p>Lorem ipsum dolor sit amet, consectetur adipiscing elit. Aliquam semper metus id blandit posuere. Duis sem urna, vulputate et aliquam feugiat, sagittis nec tortor. Nunc erat diam, pharetra nec est ac, faucibus adipiscing ligula. Quisque vulputate nulla nisi. Aenean elit elit, luctus sit amet leo vitae, aliquam venenatis est. Mauris sollicitudin non eros vel aliquam. Phasellus rutrum mi nec risus imperdiet viverra. Morbi ut mauris quis metus ornare aliquam. Aenean metus risus, tincidunt sed tellus vel, ullamcorper gravida mi. Suspendisse ultrices erat id ipsum laoreet, eget luctus erat eleifend. Sed ac ipsum ligula. Sed volutpat sapien sit amet tellus condimentum, sed porttitor leo sollicitudin. Suspendisse porta lorem</p>
  </article>
</body>
</html>
```